CONTACT US Page and design for website

We need a contact us page for our website. We would like it to have a message area, a map, our information, etc.

Please see the text attachment for what we are looking for. We need to have something that is creative and interesting, modern and professional.

We believe that a contact US page should be very creative because everyone clicks that to contact us. We want it to be super professional, attention grabbing, pleasing to the eye.

PLEASE KEEP THE HEADER AND FOOTER THE SAME, ONLY THE ACTUAL CONTACT US PAGE NEEDS TO BE WORKED ON. THANKS!
We are excited to work with designers for this project.

Target Market(s)

Clients in technology business

Industry/Entity Type

Information Technology

Number of Pages Required

1 page

Font styles to use
Serif

Requirements
Must have
• CHECK THE TEXT ATTACHMENT PLEASE
• Must stay within our design colors and theme.
Nice to have
• see attachment
Should not have
• it should be special

```html
<!DOCTYPE html>
<html lang="en">
<head>
<meta charset="utf-8">
<title>Contact Us – Kestrel Labs</title>
<link rel="stylesheet" href="https://fonts.googleapis.com/css2?family=Open+Sans:ital,wght@0,400;0,600;0,700;1,700&family=Arimo:wght@400;700&family=Poiret+One&display=swap">
<style>
:root{
  --teal:#2bbfae;
  --teal-dark:#1f9c9b;
  --ink:#111;
  --text:#444;
  --muted:#777;
  --line:#c9c9c9;
  --panel:#f0f0f0;
  --field:#f3f3f3;
  --footer:#a5a5a5;
  --footer-low:#8e8e8e;
  --white:#fff;
  --dark:#2a2a2a;
}
*{margin:0;padding:0;box-sizing:border-box}
html,body{width:894px;height:1200px;overflow:hidden;background:var(--white)}
.page{position:relative;width:894px;height:1200px;font-family:"Open Sans",sans-serif;color:var(--text)}
.abs{position:absolute;white-space:nowrap}

/* header */
.brand{left:48px;top:20px;display:flex;align-items:center;gap:10px}
.brand-dot{width:36px;height:36px;border-radius:50%;background:var(--teal)}
.brand-name{font-size:22px;letter-spacing:2px;color:var(--teal-dark);font-weight:400}
.account-tab{left:707px;top:0;width:141px;height:25px;background:#a3a3a3;border-radius:0 0 14px 14px;display:flex;font-size:8px;color:#333}
.account-tab span{flex:1;text-align:center;line-height:25px}
.account-tab span+span{background:#b5b5b5;border-radius:0 0 14px 0}
.ring{width:30px;height:30px;border-radius:50%;border:1px solid #cfe6e3;display:flex;align-items:center;justify-content:center}
.live-chat{left:624px;top:35px;display:flex;align-items:center;gap:8px;font-size:10.5px;color:#555}
.header-phone{left:725px;top:35px;display:flex;align-items:center;gap:10px;font-size:14px;color:#333}
.nav{left:0;top:75px;width:894px;height:37px;border-top:1px solid #e6e6e6;border-bottom:1px solid #b9dfdb}
.nav a{position:absolute;top:13px;font-size:8.5px;color:#444;text-decoration:none}
.search{left:694px;top:82px;width:122px;height:24px;border:1px solid #ccc;border-radius:12px;font-size:8px;color:#333;padding:6px 15px}
.search svg{position:absolute;right:9px;top:6px}
.cart{left:824px;top:80px;width:28px;height:28px}

/* left column */
.title{left:61px;top:138px;font-family:"Arimo",sans-serif;font-weight:700;font-size:34px;color:var(--ink)}
.label{font-size:8.5px;font-weight:700;color:var(--ink);letter-spacing:.2px}
.label::after{content:"";display:block;width:14px;height:2px;background:var(--teal);margin-top:3px}
.detail{font-size:9px;line-height:12.5px;color:#555}
.detail.lg{font-size:10.5px}
.social-row{left:65px;top:391px;display:flex;gap:10px}
.social-row i{width:9px;height:9px;background:var(--ink);display:block}
.inq{left:65px;width:211px;border-bottom:1px solid #999;padding-bottom:8px;font-size:9px;line-height:16px;color:#333}
.inq b{font-weight:600;color:var(--ink);font-size:9.5px}
.hours-title{left:65px;top:645px;font-size:10px;font-weight:700;color:var(--teal);letter-spacing:.6px}
.hours{left:65px;top:675px;font-size:9.5px;line-height:19.7px;color:#333;display:grid;grid-template-columns:76px auto}
.note{left:65px;top:788px;font-size:10.5px;font-style:italic;font-weight:700;color:var(--ink);line-height:15.5px;letter-spacing:.4px}

/* map + form */
.map{left:329px;top:112px;width:525px;height:363px;background:linear-gradient(135deg,#e6e5e1,#ededea 50%,#e0ded6)}
.map-pin{left:589px;top:267px}
.panel{left:329px;top:475px;width:525px;height:408px;background:var(--panel)}
.form-title{left:373px;top:506px;font-family:"Poiret One",sans-serif;font-size:21px;color:#222}
.field{border:1px solid #d3d3d3;background:var(--field);font-size:8px;color:#aaa;padding:15px 12px}
.submit{left:697px;top:800px;width:116px;height:34px;background:var(--dark);color:var(--white);font-size:12px;letter-spacing:2px;text-align:center;line-height:34px}

/* footer */
.footer{left:0;top:883px;width:894px;height:205px;background:var(--footer);font-family:"Arimo",sans-serif;color:var(--white)}
.footer-low{left:0;top:1088px;width:894px;height:112px;background:var(--footer-low);font-family:"Arimo",sans-serif;color:var(--white)}
.about{left:50px;top:13px;width:794px;text-align:center;font-size:11.5px;line-height:14.5px;white-space:normal}
.rule{height:1px;background:#bdbdbd}
.fcontact{font-size:11.5px;line-height:14.5px;display:flex;gap:8px}
.fnav{top:138px;font-size:13px}
.support{left:690px;top:138px;width:146px;text-align:center;font-size:13px}
.support small{display:block;font-size:7px;font-weight:700;line-height:10.5px}
.support small:first-of-type{margin-top:4px}
.fsocial{left:367px;top:15px;display:flex;gap:11px}
.fsocial span{width:28px;height:28px;border-radius:50%;border:1px solid #cfcfcf}
.copy{left:395px;top:69px;display:flex;align-items:center;gap:9px;font-size:10.5px;line-height:13px}
.copy i{width:16px;height:16px;border-radius:50%;background:#dcdcdc;display:block}
</style>
</head>
<body>
<div class="page">

  <header>
    <div class="abs brand"><span class="brand-dot"></span><span class="brand-name">KESTRELTECH</span></div>
    <div class="abs account-tab"><span>SIGN UP</span><span>LOGIN</span></div>
    <div class="abs live-chat"><span class="ring"><svg width="12" height="11" viewBox="0 0 12 11"><path d="M6 1C3 1 1 2.8 1 5c0 1 .5 2 1.3 2.6L1.8 10l2.6-1.4C5 8.8 5.5 9 6 9c3 0 5-1.8 5-4S9 1 6 1z" fill="var(--teal)"/></svg></span>LIVE CHAT</div>
    <div class="abs header-phone"><span class="ring"><svg width="12" height="12" viewBox="0 0 12 12"><path d="M2.5 1l2 2-1 1.5c.7 1.5 1.8 2.6 3.3 3.3l1.5-1 2 2L9 10.8C5 10.5 1.5 7 1.2 3z" fill="var(--teal)"/></svg></span>555-014-2200</div>
    <nav class="abs nav">
      <a style="left:46px">SERVERS</a><a style="left:102px">WORKSTATIONS</a><a style="left:188px">COMPONENTS</a>
      <a style="left:266px">VIRTUAL REALITY</a><a style="left:354px">DRONES</a><a style="left:408px">ABOUT US</a>
      <a style="left:469px">BLOG</a><a style="left:512px">RESOURCES</a><a style="left:582px">CONTACT US</a>
    </nav>
    <div class="abs search">Search<svg width="11" height="11" viewBox="0 0 11 11"><circle cx="4.5" cy="4.5" r="3.3" fill="none" stroke="var(--teal)" stroke-width="1.5"/><path d="M7 7l3 3" stroke="var(--teal)" stroke-width="1.6"/></svg></div>
    <svg class="abs cart" viewBox="0 0 28 28"><circle cx="14" cy="14" r="13" fill="none" stroke="#ccc"/><path d="M8 12h12l-1.5 6h-9z M11 12l2-3 M17 12l-2-3" fill="none" stroke="var(--teal)" stroke-width="1.4"/></svg>
  </header>

  <main>
    <h1 class="abs title">Contact Us</h1>

    <div class="abs label" style="left:65px;top:203px">OFFICE HEADQUARTERS</div>
    <div class="abs detail" style="left:65px;top:225px">Kestrel Labs, LLC.<br>4180 Orchard Ave.<br>Fairmont, CA 90210</div>
    <div class="abs label" style="left:64px;top:276px">EMAIL</div>
    <div class="abs detail lg" style="left:64px;top:295px">sales@kestreltech.com</div>
    <div class="abs label" style="left:64px;top:322px">TELEPHONE</div>
    <div class="abs detail lg" style="left:64px;top:341px">555-014-2200</div>
    <div class="abs label" style="left:64px;top:369px">STAY CONNECTED:</div>
    <div class="abs social-row"><i></i><i></i><i></i><i></i></div>

    <div class="abs inq" style="top:434px"><b>General Inquiries</b><br>(555)014-2200<br>info@kestreltech.com</div>
    <div class="abs inq" style="top:496px"><b>Sales Inquiries</b><br>(555)014-2200<br>sales@kestreltech.com</div>
    <div class="abs inq" style="top:558px"><b>Purchasing Inquiries</b><br>(555)014-2201<br>purchasing@kestreltech.com</div>

    <div class="abs hours-title">HOURS OF OPERATION</div>
    <div class="abs hours">
      <span>Monday</span><span>: 8:00am- 5:00pm</span>
      <span>Tuesday</span><span>: 8:00am- 5:00pm</span>
      <span>Wednesday</span><span>: 8:00am- 5:00pm</span>
      <span>Thursday</span><span>: 8:00am- 5:00pm</span>
      <span>Friday</span><span>: 8:00am- 5:00pm</span>
    </div>
    <p class="abs note">Our dedicated customer service<br>representatives are available 24/7 by<br>phone.</p>

    <div class="abs map" role="img" aria-label="Street map of the neighbourhood around the office, with the office location marked"></div>
    <svg class="abs map-pin" width="12" height="20" viewBox="0 0 12 20"><path d="M6 0C2.7 0 0 2.6 0 5.8 0 10 6 20 6 20s6-10 6-14.2C12 2.6 9.3 0 6 0z" fill="#e0402f"/><circle cx="6" cy="6" r="2" fill="#8a1a10"/></svg>

    <div class="abs panel"></div>
    <h2 class="abs form-title" style="font-weight:400">Message center to contact us. Must have:</h2>
    <div class="abs field" style="left:370px;top:562px;width:213px;height:40px">FIRST NAME</div>
    <div class="abs field" style="left:600px;top:562px;width:213px;height:40px">LAST NAME</div>
    <div class="abs field" style="left:370px;top:622px;width:213px;height:40px">EMAIL</div>
    <div class="abs field" style="left:600px;top:622px;width:213px;height:40px">PHONE</div>
    <div class="abs field" style="left:370px;top:682px;width:443px;height:101px">MASSAGE</div>
    <div class="abs submit">SUBMIT</div>
  </main>

  <footer>
    <div class="abs footer">
      <p class="abs about">Based in Fairmont California, Kestrel Labs offers custom servers, storage, and workstations for local businesses in Los Angeles, Beverly Hills, Thousand Oaks, Ventura, Orange County, Santa Barbara, Oxnard, Irvine, Anaheim, and San Diego. Kestrel Labs also offers such products to clients throughout the United States and Worldwide.</p>
      <div class="abs rule" style="left:268px;top:67px;width:356px"></div>
      <div class="abs fcontact" style="left:106px;top:80px"><svg width="8" height="12" viewBox="0 0 8 12"><path d="M4 0C1.8 0 0 1.7 0 3.9 0 6.6 4 12 4 12s4-5.4 4-8.1C8 1.7 6.2 0 4 0z" fill="#fff"/><circle cx="4" cy="4" r="1.5" fill="var(--footer)"/></svg><span>4180 Orchard Ave.<br>Fairmont, CA 90210</span></div>
      <div class="abs fcontact" style="left:376px;top:80px"><svg width="10" height="10" viewBox="0 0 12 12"><path d="M2.5 1l2 2-1 1.5c.7 1.5 1.8 2.6 3.3 3.3l1.5-1 2 2L9 10.8C5 10.5 1.5 7 1.2 3z" fill="#fff"/></svg><span>555-014-2200</span></div>
      <div class="abs fcontact" style="left:614px;top:80px"><svg width="11" height="9" viewBox="0 0 11 9" style="margin-top:3px"><rect width="11" height="9" fill="#fff"/><path d="M0 0l5.5 4.5L11 0" fill="none" stroke="var(--footer)"/></svg><span>sales@kestreltech.com</span></div>
      <div class="abs fnav" style="left:76px">Computer Hardware</div>
      <div class="abs fnav" style="left:283px">Drones</div>
      <div class="abs fnav" style="left:395px">Virtual Reality</div>
      <div class="abs fnav" style="left:555px">About Us</div>
      <div class="abs support">Customer Support<small>Terms and Conditions</small><small>Warranty Information</small><small>Contact Us</small><small>Return Policy</small></div>
    </div>
    <div class="abs footer-low">
      <div class="abs fsocial"><span></span><span></span><span></span><span></span></div>
      <div class="abs rule" style="left:268px;top:59px;width:356px"></div>
      <div class="abs copy"><i></i><span>Kestrel Labs, LLC.<br>Copyright © 2017</span></div>
    </div>
  </footer>

</div>
</body>
</html>
```